Catering Menu Package

I currently have a complete menu package, which we have redesigned as far as content, now I need to it put together in a catalog type format. It is essentially 10-12 pages in length, and will be sent for print production. Upon receiving a final edit
Updates

I have added an example gif to the project.

I did this free hand this basically what I am looking for. please change text and type to whatever you think would look best. This is a total rough design so, feel free to change any and everything. The text for the page is on the word documents. If you need more images let me know I am in the process of getting as many images uploaded for your use.

Reason: I figured we got a late jump with questions, so i am extending a few days .

Target Market(s)

The target market is business who wish to have catered luncheons, breakfasts , meetings

Industry/Entity Type

Catering

Requirements
Must have
• I have attached a copy of the text that what we want in the package, our logo, and i have also attached a catering package of another company to give you an idea what the finished product will be
Should not have
• It should not look identical to the example catering packages, these are for some inspiration we want our own design with the same type of look and feel

```html
<!DOCTYPE html>
<html lang="en">
<head>
<meta charset="utf-8">
<title>Desserts Menu – Field Table Caterers</title>
<link href="https://fonts.googleapis.com/css2?family=Lobster&family=Lora:ital,wght@0,400;0,700;1,400;1,700&display=swap" rel="stylesheet">
<style>
  :root {
    --backdrop: #e9e4dc;
    --paper: #e6ddd1;
    --paper-light: #efe8df;
    --orange: #f07322;
    --green: #5fb54f;
    --ink: #1a1512;
    --white: #ffffff;
    --photo-dark: #5a3424;
    --photo-mid: #b98a6a;
    --photo-light: #d9e2e3;
  }
  * { margin: 0; padding: 0; box-sizing: border-box; }
  html, body { width: 1200px; height: 800px; overflow: hidden; }
  body { background: var(--backdrop); position: relative; font-family: "Lora", Georgia, serif; color: var(--ink); }

  .menu-page {
    position: absolute; left: 332px; top: 16px; width: 566px; height: 746px;
    background: radial-gradient(ellipse at 40% 40%, var(--paper-light), var(--paper));
    overflow: hidden;
  }
  .page-art { position: absolute; inset: 0; }

  .header-rule { position: absolute; left: 0; top: 30px; width: 450px; height: 4px; background: var(--orange); }
  .section-tab {
    position: absolute; left: 137px; top: 13px; width: 145px; height: 40px;
    background: var(--orange); color: var(--white);
    font-family: "Lobster", cursive; font-size: 27px; line-height: 40px; text-align: center;
  }

  .menu-item { position: absolute; left: 20px; width: 420px; }
  .item-title { font-style: italic; color: var(--orange); font-size: 16.5px; font-weight: 400; line-height: 1.2; }
  .item-desc { font-style: italic; font-weight: 700; font-size: 13px; line-height: 1.45; }
  .item-desc.loose { line-height: 1.5; }
  .item-price { position: absolute; left: 240px; font-weight: 700; font-size: 17px; white-space: nowrap; }

  .terms-pill {
    position: absolute; left: 12px; top: 656px; width: 397px; height: 28px;
    background: var(--green); border-radius: 12px; color: var(--white);
    font-size: 9.5px; line-height: 12px; text-align: center; padding-top: 2px;
  }
  .contact-band {
    position: absolute; left: 0; top: 689px; width: 416px; height: 45px;
    background: var(--orange); color: var(--white);
  }
  .contact-call { position: absolute; left: 20px; top: 3px; font-size: 9.5px; font-style: italic; font-weight: 700; }
  .contact-phone { position: absolute; left: 32px; top: 15px; display: flex; align-items: center; gap: 6px; font-style: italic; font-weight: 700; font-size: 20px; color: var(--ink); }
  .contact-address { position: absolute; left: 240px; top: 3px; font-size: 10.5px; line-height: 14px; }

  .brand-name {
    position: absolute; left: 432px; top: 610px; width: 126px;
    display: flex; flex-direction: column; align-items: center; gap: 8px;
    font-weight: 700; font-size: 17px; line-height: 1.1; text-align: center; color: var(--ink);
  }
  .brand-square { width: 22px; height: 22px; background: var(--orange); }
</style>
</head>
<body>
  <main class="menu-page">
    <svg class="page-art" width="566" height="746" viewBox="0 0 566 746">
      <defs>
        <linearGradient id="photoTones" x1="0" y1="0" x2="0.4" y2="1">
          <stop offset="0" stop-color="var(--photo-light)"/>
          <stop offset="0.25" stop-color="var(--photo-mid)"/>
          <stop offset="0.55" stop-color="var(--photo-dark)"/>
          <stop offset="0.8" stop-color="var(--photo-mid)"/>
          <stop offset="1" stop-color="var(--photo-dark)"/>
        </linearGradient>
      </defs>
      <path role="img" aria-label="Photo of white-chocolate drizzled brownie squares on a blue patterned cloth"
            d="M448,0 H566 V519 H428 C445,470 470,420 468,330 C466,250 455,120 448,0 Z" fill="url(#photoTones)"/>
      <path d="M428,519 H566 V746 H416 C410,680 412,590 428,519 Z" fill="var(--white)"/>
    </svg>

    <div class="header-rule"></div>
    <h1 class="section-tab">Desserts</h1>

    <section class="menu-item" style="top:67px">
      <h2 class="item-title">Homemade Cookies, Brownies &amp; Blondies</h2>
      <p class="item-price" style="top:20px">$&amp;.&amp;&amp;per person</p>
    </section>

    <section class="menu-item" style="top:121px">
      <h2 class="item-title">Dessert Miniatures</h2>
      <p class="item-desc">Homemade Cookies, Brownies, Blondies, Petit Fours,<br>Miniature Chocolate Mousse Cups &amp; Crème Puffs</p>
      <p class="item-price" style="top:54px">$&amp;.&amp;&amp;per person</p>
    </section>

    <section class="menu-item" style="top:214px">
      <p class="item-desc">Strawberry Shortcake &amp; Chocolate Brownie Mousse Parfaits</p>
      <p class="item-price" style="top:16px">$&amp;.&amp;&amp;per person</p>
    </section>

    <section class="menu-item" style="top:263px">
      <h2 class="item-title">New York Style Cheesecake Bar</h2>
      <p class="item-desc" style="padding-left:2px">With warm chocolate sauce, caramel, strawberries<br>Cherries &amp; whipped topping</p>
      <p class="item-price" style="top:42px">$&amp;.&amp;&amp;per person</p>
    </section>

    <section class="menu-item" style="top:346px">
      <h2 class="item-title">Ice Cream Sundae Bar</h2>
      <p class="item-desc loose" style="padding-left:2px">Hand Dipped Ice Cream Cups.Served With Toppings:Chopped<br>Nuts, Chocolate Chips, Crushed Sandwich Cookies,Rainbow Sprinkles,<br>Cherries, Whipped Topping,Chocolate Syrup, Caramel,<br>Pineapple, Strawberry</p>
      <p class="item-price" style="top:84px">$&amp;.&amp;&amp;per person</p>
    </section>

    <section class="menu-item" style="top:465px">
      <h2 class="item-title">Chocolate Fountain</h2>
      <p class="item-desc loose">Milk Chocolate, Dark Chocolate Or White Chocolate.<br>Marshmallows, Fresh Strawberries, Bananas, Pineapple,<br>Cookies, Crispy Rice Treats, Pretzels, Angle Cake, Pound<br>Cake</p>
      <p class="item-price" style="top:84px">$&amp;.&amp;&amp;per person</p>
    </section>

    <p class="terms-pill">All Prices are per Person, with a 10 person minimum order per item chosen.<br>Local Products used when available and in season</p>

    <footer class="contact-band">
      <p class="contact-call">CALL OR EMAIL US TODAY:</p>
      <p class="contact-phone">
        <svg width="26" height="20" viewBox="0 0 26 20" aria-hidden="true">
          <path d="M2,6 C2,2 24,2 24,6 V8 H18 V6 H8 V8 H2 Z" fill="var(--ink)"/>
          <path d="M7,9 H19 L23,18 H3 Z" fill="var(--ink)"/>
          <circle cx="13" cy="13.5" r="2.6" fill="var(--orange)"/>
        </svg>
        410-555-0193
      </p>
      <address class="contact-address" style="font-style:normal">418 Harlow Lane<br>Dunmore, MD 20799<br>www.fieldtablecaterers.com</address>
    </footer>

    <div class="brand-name">
      <span class="brand-square"></span>
      <span>Field Table Caterers</span>
    </div>
  </main>
</body>
</html>
```